Top Real Estate teams new cards UPDATED

New Cards with MY (Im the tall guy in the middle) new pic on the front of card and my team pic on the back of card. Also my team name on the front of the card (marlow and partners) and brokerage name on the back (harborline real estate group) . Also the tag line "Ask about our 20 step plan" on the back of the card and "Welcome to the new way of Real Estate Sales" on the front of the card along with my phone number (951-482-3067) and email address (derek.marlow47@quillmail.net) my website (www.DerekMarlow.org) and my License number (BRE:07315294). I do like my team name colors of black and gold
Logo links are attached:
1. https://www.filevaultly.net/sh/815kqwz73hpadrx/AAG7MmK2PlR4ZqWsYnUuE_HQb?dl=0
2. https://www.filevaultly.net/sh/29c7vxm84tq015r/AACKDRLW46NeT2Gh8Vr4Jk7Yb?dl=0
Updates

Target Market(s)

Real Estate Customers

Industry/Entity Type

Real Estate

Contact Information for Business Card

Classy, yet east ro read and understand

Font styles to use
Sans Serif

Requirements
Must have
• Team and brokerage name, and both slogans.
• Black and gold color scheme.
Nice to have
• Bold writing
Should not have
• cluttered feeling

```html
<!DOCTYPE html>
<html lang="en">
<head>
<meta charset="utf-8">
<title>Marlow and Partners – Business Cards</title>
<link href="https://fonts.googleapis.com/css2?family=Arimo:wght@400;700&display=swap" rel="stylesheet">
<style>
  :root {
    --gold: #c9a02a;
    --gold-deep: #b38c1f;
    --ink: #1c1c1c;
    --grey-text: #6b6b6b;
    --rule: #8a8a8a;
    --paper: #ffffff;
    --backdrop: #2b2b2b;
    --suit: #1e1e1e;
    --skin-tone: #c99a7a;
  }
  * { margin: 0; padding: 0; box-sizing: border-box; }
  html, body {
    width: 1200px; height: 950px; overflow: hidden;
    background: var(--backdrop);
    font-family: "Arimo", Arial, sans-serif;
  }
  .sheet { position: relative; width: 1200px; height: 950px; }

  .card {
    position: absolute; left: 250px; width: 700px; height: 400px;
    overflow: hidden;
    box-shadow: 0 10px 30px rgba(0,0,0,0.45);
  }

  /* Front (gold) card */
  .card--front { top: 45px; background: var(--gold); }
  .front__brokerage {
    position: absolute; left: 34px; top: 150px; width: 150px;
    color: var(--paper); font-size: 13px; line-height: 1.3; font-weight: 400;
  }
  .front__portrait {
    position: absolute; right: 0; top: 0; width: 330px; height: 400px;
    background:
      radial-gradient(ellipse 80px 95px at 120px 140px, var(--skin-tone) 0%, var(--skin-tone) 70%, transparent 72%),
      radial-gradient(ellipse 190px 170px at 190px 400px, var(--suit) 0%, var(--suit) 70%, transparent 72%),
      linear-gradient(90deg, var(--gold) 0%, var(--gold-deep) 100%);
  }
  .front__team {
    position: absolute; left: 190px; top: 250px;
    color: var(--paper); font-size: 30px; font-weight: 400;
    letter-spacing: 1px; line-height: 1.05; text-transform: uppercase;
  }
  .front__tagline {
    position: absolute; left: 190px; top: 330px;
    color: var(--paper); font-size: 17px; font-weight: 700;
  }

  /* Back (white) card */
  .card--back { top: 505px; background: var(--paper); }
  .back__slogan-strip {
    position: absolute; left: 0; top: 0; width: 52px; height: 400px;
    border-right: 2px solid var(--rule);
  }
  .back__slogan {
    position: absolute; left: 26px; top: 200px;
    transform: translate(-50%, -50%) rotate(90deg);
    white-space: nowrap;
    color: var(--gold); font-size: 15px; font-weight: 700; letter-spacing: 0.5px;
  }
  .back__name {
    position: absolute; left: 80px; top: 62px;
    color: var(--ink); font-size: 22px; font-weight: 700; letter-spacing: 0.5px;
  }
  .back__role {
    position: absolute; left: 80px; top: 92px;
    color: var(--gold); font-size: 15px;
  }
  .back__logo {
    position: absolute; left: 370px; top: 60px;
    display: flex; align-items: center; gap: 14px;
  }
  .back__logo-mark {
    width: 64px; height: 64px; border-radius: 50%; background: var(--ink); flex: none;
  }
  .back__logo-name {
    color: var(--ink); font-size: 32px; font-weight: 400; line-height: 1.05;
    text-transform: uppercase; letter-spacing: 1px;
  }
  .back__contact {
    position: absolute; left: 80px; top: 250px;
    list-style: none; color: var(--grey-text); font-size: 15px; line-height: 1.65;
  }
</style>
</head>
<body>
<main class="sheet">

  <section class="card card--front" aria-label="Front of card">
    <p class="front__brokerage">Harborline Real Estate Group</p>
    <div class="front__portrait" role="img" aria-label="Portrait photo of Derek Marlow in a dark suit and tie"></div>
    <h1 class="front__team">Marlow and<br>Partners</h1>
    <p class="front__tagline">Ask about our 20 step plan</p>
  </section>

  <section class="card card--back" aria-label="Back of card">
    <div class="back__slogan-strip">
      <p class="back__slogan">Welcome to the new way of Real Estate Sales</p>
    </div>
    <h2 class="back__name">DEREK MARLOW</h2>
    <p class="back__role">Owner</p>
    <div class="back__logo">
      <span class="back__logo-mark"></span>
      <span class="back__logo-name">Marlow and<br>Partners</span>
    </div>
    <ul class="back__contact">
      <li>BRE: 07315294</li>
      <li>PHONE: (951-482-3067)</li>
      <li>derek.marlow47@quillmail.net</li>
      <li>www.DerekMarlow.org</li>
    </ul>
  </section>

</main>
</body>
</html>
```